Financial Advisor needs waiting room sign

I am a financial advisor that works with a number of accountants to develop prospects. I am looking for a 18"x24" sign to hang in their office waiting rooms to help develop prospect interest in my services. My original idea was to list all of our services in a jumbled way on the sign and on the bottom have something like "Confused? We have the answers?" "Questions - We have answers" Our logo on the bottom. While I think this is still a good idea when I try to design it - it does not work. I am open to other ideas. Here is a list of our services (list in no particular order) and I will attach our logo. List: Plovance, Plovance Supplement, Plovance Advantage, Truvely, Part A, Part B, Part D, Social Security, Turning 65, Annuities, Fixed Index Annuities, Rollovers, 401k, 403b, Investments, Stock Market, Mutual Funds, Term Insurance, Life Insurance, Final Expense, Long Term Care, Mortgage Protection, 403B / 457 Not for Profit Set Up, 403B / TSA Plans, Annuities, Asset Protection, Charitable Giving, College Funding, Estate Planning, Fixed Indexed Annuities, Guaranteed Income, IRA & 401(K) Assets and Planning, IRA, 401(K), 403(B) Rollovers, Lifetime Income Planning, Retirement Income Planning, Safe Money Options, Social Security, Tactical Asset Allocation

```html
<!DOCTYPE html>
<html lang="en">
<head>
<meta charset="utf-8">
<title>Halvorne Capital – Waiting Room Sign</title>
<link href="https://fonts.googleapis.com/css2?family=Arimo:wght@400;700&family=Roboto+Condensed:wght@700&family=Roboto:wght@300;400;700&family=Archivo+Black&display=swap" rel="stylesheet">
<style>
  :root{
    --green:#4a6e08;
    --blue:#064b6c;
    --grey:#e6e6e6;
    --white:#ffffff;
  }
  *{margin:0;padding:0;box-sizing:border-box;}
  html,body{width:906px;height:1200px;overflow:hidden;background:var(--white);}
  .sign{position:relative;width:906px;height:1200px;overflow:hidden;background:var(--white);}
  .sign__wave{position:absolute;left:0;top:0;width:906px;height:880px;}
  .cloud{position:absolute;inset:0;color:var(--white);}
  .term{position:absolute;white-space:nowrap;line-height:1;font-family:"Arimo",Arial,sans-serif;}
  .term--light{font-family:"Roboto",Arial,sans-serif;font-weight:300;}
  .term--regular{font-family:"Roboto",Arial,sans-serif;font-weight:400;}
  .term--bold{font-weight:700;}
  .term--cond{font-family:"Roboto Condensed","Arial Narrow",sans-serif;font-weight:700;letter-spacing:-0.02em;}
  .term--up{writing-mode:vertical-rl;transform:rotate(180deg);}
  .term--stack{white-space:normal;}

  .tagline{position:absolute;left:0;top:936px;width:906px;text-align:center;
    font-family:"Archivo Black","Arial Black",sans-serif;font-size:45px;line-height:1;color:var(--blue);letter-spacing:0.005em;}
  .brand{position:absolute;left:0;top:1072px;width:906px;display:flex;justify-content:center;align-items:center;gap:20px;}
  .brand__dot{width:72px;height:72px;border-radius:50%;background:var(--green);}
  .brand__name{font-family:"Arimo",Arial,sans-serif;font-weight:700;font-size:34px;letter-spacing:0.04em;color:var(--green);}
</style>
</head>
<body>
<main class="sign">
  <svg class="sign__wave" viewBox="0 0 906 880" aria-hidden="true">
    <path d="M0,0 H906 V678 Q560,850 0,862 Z" fill="var(--grey)"/>
    <path d="M0,0 H906 V651 Q560,828 0,842 Z" fill="var(--blue)"/>
    <path d="M0,0 H906 V622 Q560,798 0,808 Z" fill="var(--green)"/>
  </svg>

  <section class="cloud" aria-label="Services">
    <span class="term term--regular" style="left:48px;top:57px;font-size:61px;">Social Security</span>
    <span class="term term--cond" style="left:484px;top:68px;font-size:43px;">Estate Planning</span>
    <span class="term term--regular" style="right:50px;top:88px;font-size:28px;">Life</span>
    <span class="term term--regular" style="right:50px;top:120px;font-size:28px;">Insurance</span>
    <span class="term term--light" style="left:91px;top:118px;font-size:28px;">Part A</span>
    <span class="term term--bold" style="left:170px;top:118px;font-size:45px;">401(K)</span>
    <span class="term term--regular" style="left:464px;top:120px;font-size:22px;">Turning 65 Annuities</span>
    <span class="term term--bold" style="left:459px;top:147px;font-size:57px;letter-spacing:-0.02em;">Stock Market</span>

    <span class="term term--regular term--up" style="left:57px;top:136px;font-size:24px;">Truvely</span>
    <span class="term term--light term--up" style="left:57px;top:259px;font-size:26px;">Part D</span>
    <span class="term term--bold term--up" style="left:88px;top:155px;font-size:66px;">IRA</span>
    <span class="term term--light" style="left:103px;top:279px;font-size:18px;">Part B</span>
    <span class="term term--cond" style="left:159px;top:164px;font-size:60px;">Mutual</span>
    <span class="term term--cond" style="left:170px;top:222px;font-size:60px;">Funds</span>
    <span class="term term--cond term--up" style="left:331px;top:125px;font-size:23px;">Final Expense</span>
    <span class="term term--light term--up" style="left:363px;top:126px;font-size:28px;">Fixed Indexed Annuities</span>
    <span class="term term--bold term--up" style="left:398px;top:133px;font-size:58px;">Plovance</span>

    <span class="term term--regular" style="left:482px;top:213px;font-size:29px;">College Funding</span>
    <span class="term term--cond" style="left:459px;top:250px;font-size:43px;">Long Term Care</span>
    <span class="term term--light term--up" style="left:724px;top:212px;font-size:38px;">Safe Money</span>
    <span class="term term--bold" style="left:781px;top:218px;font-size:36px;">403b</span>
    <span class="term term--light term--up" style="left:778px;top:287px;font-size:38px;">Options</span>
    <span class="term term--regular term--up" style="left:831px;top:266px;font-size:39px;">Asset Protection</span>
    <span class="term term--regular" style="left:466px;top:308px;font-size:28px;">Guaranteed Income</span>
    <span class="term term--bold" style="right:195px;top:345px;font-size:48px;text-align:right;line-height:54px;">Plovance<br>Advantage</span>

    <span class="term term--cond" style="right:666px;top:305px;font-size:36px;text-align:right;line-height:42px;">Plovance<br>Supplement</span>
    <span class="term term--light" style="left:106px;top:391px;font-size:28px;">Annuities</span>
    <span class="term term--regular term--up" style="left:258px;top:296px;font-size:24px;">Retirement</span>
    <span class="term term--light term--up" style="left:290px;top:296px;font-size:24px;">Income</span>
    <span class="term term--light term--up" style="left:320px;top:296px;font-size:24px;">Planning</span>

    <span class="term term--cond" style="left:40px;top:422px;font-size:63px;letter-spacing:-0.03em;">Investments</span>
    <span class="term term--regular" style="left:407px;top:454px;font-size:26px;">403B / 457 Not for Profit Set Up</span>

    <span class="term term--bold term--up" style="left:60px;top:494px;font-size:23px;">403B / TSA Plans</span>
    <span class="term term--regular term--up" style="left:101px;top:496px;font-size:30px;">403(B) Rollovers</span>
    <span class="term term--bold" style="left:132px;width:224px;top:490px;font-size:46px;text-align:center;line-height:57px;">Lifetime<br>Income<br>Planning</span>
    <span class="term term--regular" style="left:132px;width:224px;top:672px;font-size:28px;text-align:center;line-height:43px;">Mortgage<br>Protection</span>
    <span class="term term--bold term--up" style="left:345px;top:494px;font-size:28px;">Charitable Giving</span>
    <span class="term term--cond term--up" style="left:391px;top:499px;font-size:47px;">Rollovers</span>
    <span class="term term--regular term--up" style="left:454px;top:503px;font-size:29px;">Term Insurance</span>
    <span class="term term--bold" style="left:496px;top:494px;font-size:46px;line-height:53px;">Tactical<br>Asset<br>Allocation</span>
    <span class="term term--light term--up term--stack" style="left:664px;top:518px;height:98px;font-size:22px;line-height:30px;text-align:end;">IRA &amp;<br>401(K)<br>Assets<br>and<br>Planning</span>
  </section>

  <p class="tagline">Confused? We have the answers.</p>

  <footer class="brand">
    <span class="brand__dot" aria-hidden="true"></span>
    <span class="brand__name">HALVORNE CAPITAL</span>
  </footer>
</main>
</body>
</html>
```